依頼詳細
ターゲット層が50代以上になる予想ですので、ネットよりチラシの方が分かりやすいと思っております。

イメージしているチラシは下記に貼っときますのでご確認ください。
デザインイメージとしては、
・明るいチラシ
・カテゴリー分けされた分かりやすいチラシ
・チラシ保管による割引
割引内容(5000円以上で500円引き、10000円以上で1000円引き)
・一目でわかる大きな不用品回収、買取の文言
・ビフォー、アフターの写真を掲載
・自社キャラクターの添付(下記に添付しております)
・キャラクターでわかりやすいスケジュールの流れ
・回収、買取実績の値段詳細を掲載(数字はこちらで記載するので空欄でも大丈夫です。¥00,000~と入れていただけばと思います。)

以上多くなりましたがこちらをできるだけ加えて作成して頂くと幸いです。
細か点や、不明点が生じると思います。お気軽にご質問下さい。
よろしくお願い致します。
記載項目
社名:売りナビ福岡天神店/電話番号:0120-47-3286/HP:https://urinavi-example.jp/area/fukuokatenjin//住所:〒812-4093 福岡県糟屋郡粕屋町桜見台東3丁目8−24
サイズ
B4
ページ数
両面
希望イメージ
シンプル 複雑
単色 カラフル
暗い 明るい
日常 高級
遊び心 厳粛
未来的 伝統的
女性的 男性的
希望する色
設定なし
納品ファイル
• イラストレーター形式 (.ai)
補足説明
自社キャラクターの横にこの方が行きますみたいな吹き出しを入れて頂きたいです。

添付資料の1枚目、2枚目が理想に近いです。
こちらにできるだけ近づけて頂いたらと思います。
よろしくお願い致します。

イメージに一番近く最高な出来でした。

皆様この度はご提案いただき誠に有難うございます。
今後また、依頼することあればよろしくお願い致します。

森下

```html
<!DOCTYPE html>
<html lang="ja">
<head>
<meta charset="utf-8">
<title>売りナビ福岡天神店 不用品回収・買取チラシ</title>
<link href="https://fonts.googleapis.com/css2?family=Noto+Sans+JP:wght@400;700;900&family=Noto+Serif+JP:wght@900&display=swap" rel="stylesheet">
<style>
:root{
  --red:#e60012;
  --pink:#e5306f;
  --yellow:#fff100;
  --pale:#fff8d6;
  --ink:#1a1a1a;
  --cream:#fffdf3;
  --gold:#f5b400;
}
*{box-sizing:border-box;margin:0;padding:0}
html,body{width:846px;height:1200px;overflow:hidden;background:#fff}
body{font-family:"Noto Sans JP",sans-serif;color:var(--ink)}
.flyer{position:relative;width:846px;height:1200px;overflow:hidden;background:var(--cream)}
.abs{position:absolute}

/* header */
.header{left:0;top:0;width:846px;height:210px;background:linear-gradient(#fff,#fff6ec)}
.lead-big{left:16px;top:6px;font-weight:900;line-height:1;color:var(--pink)}
.lead-big .l1{font-size:50px;color:var(--red)}
.lead-big .l2{font-size:50px;display:block;margin-top:4px}
.to{left:246px;top:34px;width:62px;height:62px;border-radius:50%;background:var(--pink);color:#fff;font:900 44px/62px "Noto Sans JP",sans-serif;text-align:center}
.fuyou{left:316px;top:6px;font:900 96px/1 "Noto Sans JP",sans-serif;color:var(--red);letter-spacing:-2px}
.kaishu{left:620px;top:8px;display:flex;flex-direction:column;gap:4px}
.kaishu span{width:40px;height:44px;background:var(--red);color:#fff;font:900 30px/44px "Noto Sans JP",sans-serif;text-align:center}
.badge-price{left:676px;top:10px;width:150px;height:90px;background:var(--yellow);border:4px solid var(--red);border-radius:12px;text-align:center;color:var(--red);font-weight:900}
.badge-price b{display:block;font-size:36px;line-height:46px}
.badge-price small{display:block;font-size:26px;line-height:32px;color:var(--ink)}
.intro{left:18px;top:120px;width:260px;font-size:13px;line-height:1.5;font-weight:700}
.phone-ok{left:290px;top:118px;font:900 42px/1.1 "Noto Sans JP",sans-serif;letter-spacing:-1px}
.phone-ok em{font-style:normal;color:var(--red)}

/* services */
.services{left:14px;top:206px;width:818px;display:grid;grid-template-columns:1fr 1fr;gap:8px 14px;list-style:none}
.service{display:flex;align-items:center;gap:10px;height:64px;padding-left:8px;background:linear-gradient(transparent 55%,var(--yellow) 55%)}
.service svg{flex:none}
.service span{font:900 52px/1 "Noto Sans JP",sans-serif;color:var(--red);letter-spacing:2px}

/* before / after */
.photos{left:0;top:350px;width:846px;height:300px}
.photo{position:absolute;border:3px solid #fff;box-shadow:0 2px 6px rgba(0,0,0,.25)}
.photo.before{left:14px;top:36px;width:300px;height:200px;background:linear-gradient(135deg,#a58a6a,#d9c3a1 60%,#8c6f52)}
.photo.after{left:336px;top:12px;width:300px;height:234px;background:linear-gradient(160deg,#f4f1ea,#d9d4c8 55%,#b7a98f)}
.photo.staff{left:652px;top:0;width:194px;height:260px;border:none;box-shadow:none;background:linear-gradient(#f3e7e9,#e8b9c6)}
.tag{position:absolute;top:0;font:900 22px/1 "Noto Sans JP",sans-serif;color:var(--red);background:#fff;padding:4px 10px;border:3px solid var(--red);border-radius:20px}
.tag.t1{left:46px}.tag.t2{left:500px}
.caption{left:150px;top:612px;width:520px;height:32px;background:var(--yellow);text-align:center;font:900 18px/32px "Noto Sans JP",sans-serif}

/* buy headline */
.buy-title{left:0;top:652px;width:846px;height:86px;text-align:center;font:900 54px/86px "Noto Sans JP",sans-serif;color:var(--red);letter-spacing:1px}
.buy-title .hl{display:inline-block;background:var(--yellow);border-radius:50%;padding:0 6px;line-height:70px}

/* items */
.items{left:12px;top:738px;width:486px;height:166px;background:linear-gradient(120deg,#efe3cf,#d8c1a2 50%,#c6d2dc)}
.items-badge{left:22px;top:748px;width:74px;height:74px;border-radius:50%;background:var(--red);color:#fff;font:900 20px/1.15 "Noto Sans JP",sans-serif;text-align:center;padding-top:14px}
.items-list{left:106px;top:748px;width:384px;font:900 23px/1.45 "Noto Sans JP",sans-serif;color:var(--red);text-shadow:0 0 3px #fff,0 0 3px #fff,0 0 3px #fff}

.results{left:508px;top:738px;width:326px;height:166px;background:#fff;border:3px solid var(--red)}
.results h3{background:var(--red);color:#fff;font:900 20px/30px "Noto Sans JP",sans-serif;text-align:center}
.results p.note{font-size:10px;line-height:14px;text-align:center;font-weight:700}
.results table{width:100%;border-collapse:collapse;font-size:10.5px;font-weight:700}
.results td{border-top:1px dotted #bbb;padding:0 6px;height:11.6px;line-height:11.6px}
.results td.price{text-align:right;color:var(--red)}

/* band */
.band{left:0;top:908px;width:846px;height:46px;background:var(--red);display:flex;align-items:center;gap:14px;padding-left:14px}
.band .hi{font:900 24px/1 "Noto Sans JP",sans-serif;color:var(--yellow)}
.band .catch{font:900 30px/1 "Noto Serif JP",serif;color:#fff}
.band .cats{background:var(--yellow);color:var(--red);font:900 18px/28px "Noto Sans JP",sans-serif;padding:0 10px}

/* footer */
.footer{left:0;top:954px;width:846px;height:246px;background:var(--pale)}
.shop{left:14px;top:966px;width:400px;height:224px;background:#fff;border:3px solid var(--red);border-radius:10px}
.shop .svc{position:absolute;left:12px;top:10px;background:var(--red);color:#fff;font:900 18px/28px "Noto Sans JP",sans-serif;padding:0 12px;border-radius:4px}
.shop .name{position:absolute;left:12px;top:44px;font:900 46px/1 "Noto Sans JP",sans-serif;color:var(--red)}
.shop .mark{position:absolute;left:300px;top:14px;width:80px;height:80px;border-radius:50%;background:var(--red)}
.shop .branch{position:absolute;left:12px;top:96px;font:900 30px/1 "Noto Sans JP",sans-serif}
.shop .tel{position:absolute;left:12px;top:136px;display:flex;align-items:center;gap:6px;font:900 40px/1 "Noto Sans JP",sans-serif;color:var(--red);letter-spacing:-1px}
.shop .info{position:absolute;left:12px;top:182px;font-size:10px;line-height:1.45;font-weight:700}

.flow{left:426px;top:966px;width:406px;height:224px;background:#fff;border:3px solid var(--gold);border-radius:10px}
.flow h3{background:var(--gold);color:#fff;text-align:center;font:900 22px/34px "Noto Sans JP",sans-serif}
.flow .sub{text-align:center;color:var(--red);font-size:12px;font-weight:900;line-height:20px}
.steps{display:flex;justify-content:space-between;padding:6px 10px 0}
.step{width:86px;text-align:center}
.step .num{display:block;width:30px;height:30px;margin:0 auto 4px;border-radius:50%;background:var(--red);color:#fff;font:900 16px/30px "Noto Sans JP",sans-serif}
.step .pic{height:58px;border-radius:6px;background:linear-gradient(#fff3c4,#ffd77a)}
.step p{font-size:11px;line-height:1.35;font-weight:700;margin-top:4px}
.step-arrow{align-self:center;color:var(--red);font-weight:900;font-size:16px}
</style>
</head>
<body>
<div class="flyer">

  <section class="abs header"></section>
  <h1 class="abs lead-big"><span class="l1">大変な</span><span class="l2">お片付け</span></h1>
  <div class="abs to">と</div>
  <div class="abs fuyou">不用品</div>
  <div class="abs kaishu"><span>回</span><span>収</span></div>
  <div class="abs badge-price"><b>格安</b><small>有料</small></div>
  <p class="abs intro">一人ではどうしようも出来ない大きい家具や、家電、遺品整理等の片付け、引越しや店舗閉店時の不要品なども…</p>
  <p class="abs phone-ok">電話一本で<em>無料見積もり</em>OK</p>

  <ul class="abs services">
    <li class="service"><svg width="46" height="46" viewBox="0 0 46 46"><rect x="3" y="3" width="40" height="40" fill="#fff" stroke="#e60012" stroke-width="4"/><path d="M10 22l9 10 17-22" fill="none" stroke="#e60012" stroke-width="6" stroke-linecap="round"/></svg><span>遺品整理</span></li>
    <li class="service"><svg width="46" height="46" viewBox="0 0 46 46"><rect x="3" y="3" width="40" height="40" fill="#fff" stroke="#e60012" stroke-width="4"/><path d="M10 22l9 10 17-22" fill="none" stroke="#e60012" stroke-width="6" stroke-linecap="round"/></svg><span>生前整理</span></li>
    <li class="service"><svg width="46" height="46" viewBox="0 0 46 46"><rect x="3" y="3" width="40" height="40" fill="#fff" stroke="#e60012" stroke-width="4"/><path d="M10 22l9 10 17-22" fill="none" stroke="#e60012" stroke-width="6" stroke-linecap="round"/></svg><span>引越整理</span></li>
    <li class="service"><svg width="46" height="46" viewBox="0 0 46 46"><rect x="3" y="3" width="40" height="40" fill="#fff" stroke="#e60012" stroke-width="4"/><path d="M10 22l9 10 17-22" fill="none" stroke="#e60012" stroke-width="6" stroke-linecap="round"/></svg><span>店舗整理</span></li>
  </ul>

  <section class="abs photos">
    <div class="photo before" role="img" aria-label="片付け前の散らかった部屋の写真"></div>
    <div class="photo after" role="img" aria-label="片付け後のすっきりした部屋の写真"></div>
    <div class="photo staff" role="img" aria-label="笑顔のスタッフの写真"></div>
    <span class="tag t1">片付け前</span>
    <span class="tag t2">片付け後</span>
    <svg class="abs" style="left:300px;top:120px" width="50" height="50" viewBox="0 0 50 50"><path d="M4 16h24V4l20 21-20 21V34H4z" fill="#e60012" stroke="#fff" stroke-width="3"/></svg>
  </section>
  <p class="abs caption">状況にもよりますが2~3時間でキレイになります!</p>

  <h2 class="abs buy-title">どんなものでも<span class="hl">高価</span>買取します!</h2>

  <section class="abs items" role="img" aria-label="家電やブランド品など買取品目の写真"></section>
  <div class="abs items-badge">買取<br>品目</div>
  <p class="abs items-list">家電・ブランド家具・骨董品・着物・携帯・タブレット・貴金属・宝石・切手・お酒・楽器・おもちゃ・ホビー・ゲーム機・ソフト等</p>

  <section class="abs results">
    <h3>回収、買取実績</h3>
    <p class="note">※参考買取価格</p>
    <table>
      <tr><td>ミナト電機 ドラム式洗濯機</td><td class="price">¥00,000~</td></tr>
      <tr><td>コウセイ光学 デジタル一眼レフ</td><td class="price">¥00,000~</td></tr>
      <tr><td>ヒビキ音響 液晶テレビ</td><td class="price">¥00,000~</td></tr>
      <tr><td>エアリス コードレス掃除機</td><td class="price">¥00,000~</td></tr>
      <tr><td>クロノア 腕時計</td><td class="price">¥00,000~</td></tr>
      <tr><td>メゾン・リュクス バッグ</td><td class="price">¥00,000~</td></tr>
      <tr><td>ダイニングセット テーブル</td><td class="price">¥00,000~</td></tr>
      <tr><td>冷蔵庫 大型</td><td class="price">¥00,000~</td></tr>
      <tr><td>ゲーム機 本体一式</td><td class="price">¥00,000~</td></tr>
    </table>
  </section>

  <section class="abs band">
    <span class="hi">高額査定!</span>
    <span class="catch">高く買わせてください!</span>
    <span class="cats">貴金属・ブランド・金券・切手</span>
  </section>

  <section class="abs footer"></section>
  <section class="abs shop">
    <span class="svc">出張買取サービス</span>
    <span class="mark"></span>
    <p class="name">売りナビ</p>
    <p class="branch">福岡天神店</p>
    <p class="tel"><svg width="34" height="34" viewBox="0 0 24 24"><path d="M6.6 10.8a15 15 0 0 0 6.6 6.6l2.2-2.2a1 1 0 0 1 1-.25 11.4 11.4 0 0 0 3.6.57 1 1 0 0 1 1 1V20a1 1 0 0 1-1 1A17 17 0 0 1 3 4a1 1 0 0 1 1-1h3.5a1 1 0 0 1 1 1c0 1.25.2 2.45.57 3.6a1 1 0 0 1-.25 1z" fill="#e60012"/></svg>0120-47-3286</p>
    <p class="info">〒812-4093 福岡県糟屋郡粕屋町桜見台東3丁目8−24<br>https://urinavi-example.jp/area/fukuokatenjin/ 受付 10:00~18:00</p>
  </section>

  <section class="abs flow">
    <h3>出張買取の流れ</h3>
    <p class="sub">安心・安全を第一に考えた出張買取</p>
    <div class="steps">
      <div class="step"><span class="num">1</span><div class="pic" role="img" aria-label="電話で申し込むキャラクターのイラスト"></div><p>お電話で<br>お申し込み</p></div>
      <span class="step-arrow">▶</span>
      <div class="step"><span class="num">2</span><div class="pic" role="img" aria-label="訪問するキャラクターのイラスト"></div><p>ご指定日に<br>ご訪問</p></div>
      <span class="step-arrow">▶</span>
      <div class="step"><span class="num">3</span><div class="pic" role="img" aria-label="査定するキャラクターのイラスト"></div><p>その場で<br>無料査定</p></div>
      <span class="step-arrow">▶</span>
      <div class="step"><span class="num">4</span><div class="pic" role="img" aria-label="現金を渡すキャラクターのイラスト"></div><p>即日現金<br>お支払い</p></div>
    </div>
  </section>

</div>
</body>
</html>
```